Holiday Rental Company Flyer Design (DL not A5)

Note from PixelFolk Administration: The category sizing selected is A5, however the project requires DL sized artwork. Please refer to the DL template link below while the 'Special Requirements' are updated accordingly.

Project Brief:
We need a double sided DL flyer designed for an up market Holiday Rental Company that portrays a personalised approach to property management. These are to be used for letter box drops to homes we're specifically targeting so the design should be modern, complimentary colour palette, uncluttered & visually appealing.

Please Download the DL Template from Quillmark here: http://www.quillmark.com.au/qm/ns/propath/UploadResources.aspx?selectedTab=0?pfid=BFB&pf_id=BFB&xnav=easypath-upload-image#Templates

Target Market(s)

Wealthy Home Owners

Industry/Entity Type

It Company

Font styles to use
Other font styles liked:
• Avant Garde Extra Light & Demi

Colors
33b8a4

Requirements
Must have
• DL Flyer sizes (210mm width x 99mm width, plus 3mm bleed)
• Front: Logo, Main Image & Grab
• Back: Contact Details & Brief Description of our business
• Images: Ideally the main image should be the house with the pool but alternatively a lifestyle images could also be used.
Nice to have
• A creative designer!
Should not have
• Clutter & busy designs

```html
<!DOCTYPE html>
<html lang="en">
<head>
<meta charset="utf-8">
<title>Harbourline Stays – DL Flyer</title>
<link rel="stylesheet" href="https://fonts.googleapis.com/css2?family=Jost:wght@300;400&display=swap">
<style>
  :root {
    --stage: #000000;
    --paper: #ffffff;
    --teal: #10b08c;
    --teal-soft: #4cc3b0;
    --ink-grey: #6d6e70;
    --rule-grey: #c4c4c4;
    --white: #ffffff;
  }
  * { box-sizing: border-box; margin: 0; padding: 0; }
  html, body {
    width: 1200px; height: 1183px; overflow: hidden;
    background: var(--stage);
    font-family: "Jost", "Century Gothic", sans-serif;
  }
  .canvas { position: relative; width: 1200px; height: 1183px; }

  .flyer { position: absolute; top: 84px; width: 491px; height: 1015px; overflow: hidden; }
  .flyer--front { left: 84px; background: var(--paper); }
  .flyer--back { left: 625px; background: var(--teal); color: var(--white); }

  /* Front */
  .brand {
    position: absolute; top: 84px; left: 0; width: 100%;
    text-align: center; color: var(--teal);
    font-weight: 300; font-size: 28px; letter-spacing: 3px; line-height: 31px;
    text-transform: uppercase;
  }
  .brand__dot {
    position: absolute; top: 157px; left: 227px;
    width: 36px; height: 36px; border: 2px solid var(--teal); border-radius: 50%;
  }
  .photo { position: absolute; }
  .photo--pool { left: 69px; top: 265px; width: 352px; height: 202px;
    background: linear-gradient(180deg, #2a2a5a 0%, #4a3f7a 45%, #2f6fd0 80%, #3aa0e8 100%); }
  .photo--basin { left: 69px; top: 475px; width: 274px; height: 194px;
    background: linear-gradient(160deg, #c9c9c9 0%, #aeb1b3 50%, #e2e2e2 100%); }
  .photo--bedroom { left: 121px; top: 677px; width: 300px; height: 200px;
    background: linear-gradient(170deg, #d8c8a8 0%, #c4a882 40%, #d8d050 70%, #e8a070 100%); }
  .accent { position: absolute; }
  .accent--right { left: 349px; top: 475px; width: 72px; height: 194px; background: var(--teal); }
  .accent--left { left: 69px; top: 677px; width: 44px; height: 200px; background: var(--teal-soft); }
  .tagline {
    position: absolute; left: 69px; top: 933px;
    font-size: 16.5px; font-weight: 400; color: var(--ink-grey); letter-spacing: 0.3px;
  }
  .tagline-rule { position: absolute; left: 69px; top: 969px; width: 352px; height: 3px; background: var(--rule-grey); }

  /* Back */
  .section-band {
    position: absolute; left: 0; top: 55px; width: 100%; height: 30px;
    background: var(--white); color: var(--teal);
    text-align: center; font-size: 19px; line-height: 30px; font-weight: 400;
  }
  .intro {
    position: absolute; left: 28px; top: 114px; width: 434px;
    font-size: 16px; line-height: 20px; font-weight: 400;
  }
  .intro p { margin-bottom: 20px; }
  .intro .line { display: block; white-space: nowrap; }
  .intro .line--full { text-align: justify; text-align-last: justify; white-space: normal; }
  .contacts { position: absolute; left: 28px; top: 446px; list-style: none; }
  .contacts li { display: flex; align-items: center; height: 36px; margin-bottom: 8px; font-size: 15px; font-weight: 300; }
  .contacts__icon {
    width: 36px; height: 36px; background: var(--white); margin-right: 14px;
    display: flex; align-items: center; justify-content: center;
  }
  .photo--flowers { left: 22px; top: 647px; width: 448px; height: 344px;
    background: linear-gradient(90deg, #8a7a68 0%, #a69580 45%, #d8cfc0 80%, #e0603a 92%, #c84a2a 100%); }
</style>
</head>
<body>
<main class="canvas">

  <section class="flyer flyer--front" aria-label="Flyer front">
    <h1 class="brand">Harbourline<br>Stays</h1>
    <span class="brand__dot" aria-hidden="true"></span>

    <div class="photo photo--pool" role="img" aria-label="Modern house at dusk with lit lap pool"></div>
    <div class="photo photo--basin" role="img" aria-label="Bathroom basin with white flowers in a vase"></div>
    <div class="accent accent--right"></div>
    <div class="accent accent--left"></div>
    <div class="photo photo--bedroom" role="img" aria-label="Bed with yellow cushions and colourful quilt"></div>

    <p class="tagline">Holiday Rental Management with a difference</p>
    <div class="tagline-rule"></div>
  </section>

  <section class="flyer flyer--back" aria-label="Flyer back">
    <h2 class="section-band">What we do differently!</h2>

    <div class="intro">
      <p>
        <span class="line line--full">Rather than relying upon a key safe or a central pick-up</span>
        <span class="line line--full">destination, a ‘Harbourline Stays’ staff member will greet</span>
        <span class="line">guests upon arrival.</span>
      </p>
      <p>
        <span class="line line--full">Our ‘Meet &amp; Greet’ service provides home owners with an</span>
        <span class="line">increased level of Security and also allows us to:</span>
      </p>
      <p>
        <span class="line line--full">Prepare the home for their arrival (lights, heaters, music</span>
        <span class="line">etc.)</span>
      </p>
      <p>
        <span class="line line--full">Establish a rapport &amp; help facilitate future bookings Reiter-</span>
        <span class="line line--full">ate their responsibilities to ensure the return of their bond</span>
      </p>
      <p>
        <span class="line line--full">If you’d like to know what your property could achieve or</span>
        <span class="line">require additional information, please contact us on:</span>
      </p>
    </div>

    <ul class="contacts">
      <li>
        <span class="contacts__icon">
          <svg width="14" height="14" viewBox="0 0 24 24"><path fill="#10b08c" d="M6.6 10.8a15 15 0 0 0 6.6 6.6l2.2-2.2c.3-.3.7-.4 1-.2 1.1.4 2.3.6 3.6.6.6 0 1 .4 1 1V20c0 .6-.4 1-1 1A17 17 0 0 1 3 4c0-.6.4-1 1-1h3.5c.6 0 1 .4 1 1 0 1.3.2 2.5.6 3.6.1.3 0 .7-.2 1z"/></svg>
        </span>(03)5012 3476
      </li>
      <li>
        <span class="contacts__icon">
          <svg width="14" height="12" viewBox="0 0 24 18"><rect x="1" y="1" width="22" height="16" fill="#10b08c"/><path d="M1 1l11 9 11-9" fill="none" stroke="#fff" stroke-width="2"/></svg>
        </span>stay@harbourlinestays.com.au
      </li>
      <li>
        <span class="contacts__icon">
          <svg width="14" height="14" viewBox="0 0 24 24" fill="none" stroke="#10b08c" stroke-width="2"><circle cx="12" cy="12" r="10"/><ellipse cx="12" cy="12" rx="4" ry="10"/><path d="M2 12h20"/></svg>
        </span>harbourlinestays.com.au
      </li>
      <li>
        <span class="contacts__icon">
          <svg width="12" height="16" viewBox="0 0 24 32"><path fill="#10b08c" d="M12 0a11 11 0 0 0-11 11c0 8 11 21 11 21s11-13 11-21A11 11 0 0 0 12 0zm0 15a4 4 0 1 1 0-8 4 4 0 0 1 0 8z"/></svg>
        </span>PO Box 18, Seacliff Victoria 3999
      </li>
    </ul>

    <div class="photo photo--flowers" role="img" aria-label="Bird of paradise flowers in a glass vase with tea light candles"></div>
  </section>

</main>
</body>
</html>
```